design double sided business cards - construction

************NO IMAGES OF HOME BUILDING************ONLY IMAGES OF HOME REPAIRS*****

Front -
[ WE SOLVE ALL YOUR REPAIR NEEDS] Dwelling&Lodging
Dorian Pellham - Owner

FOR A FREE QUOTE - Call 555.314.8826
DORIANPELLHAM047@[login to view URL]
[login to view URL]

(((include home repairs/landscaping imagery on the front)))

Back -
THE CORNERSTONE FIXERS - DWELLINGS&LODGING

PLUMBING -------- FLOORING
ELECTRICAL ---------- PAINTING
LANDSCAPING ----------- DRY WALL

WE CAN HELP | HOME REPAIR | MADE EASY!

GET YOUR FREE QUOTE TODAY! Call 555.314.8826

(((include imagery of home repairmen/landscapers on the back)))

You dont have to use the attached images, those are just examples

***FINAL FILES MUST BE 300DPI CMYK LAYERED PSD FILES WITH EDITABLE TEXT***
**SIZE IS US STANDARD 2X3.5 WITH AN EXTRA 0.125 ADDED TO WIDTH AND LENGTH FOR BLEED**

```html
<!DOCTYPE html>
<html lang="en">
<head>
<meta charset="utf-8">
<title>The Cornerstone Fixers – Business Cards</title>
<link rel="stylesheet" href="https://fonts.googleapis.com/css2?family=Didact+Gothic&family=Montserrat:wght@400;700;800&display=swap">
<style>
  :root {
    --backdrop: #3a3b3d;
    --card: #ffffff;
    --ink: #1c1c1c;
    --rule: #2a2a2a;
    --photo-warm-a: #f2b833;
    --photo-warm-b: #8a8f96;
    --photo-cool-a: #5f8fc9;
    --photo-cool-b: #d8dde3;
    --photo-wood-a: #c77f45;
    --photo-wood-b: #efe6dc;
  }
  * { box-sizing: border-box; margin: 0; padding: 0; }
  html, body { width: 1200px; height: 907px; overflow: hidden; }
  body {
    background: var(--backdrop);
    position: relative;
    font-family: "Didact Gothic", sans-serif;
    color: var(--ink);
  }
  .card {
    position: absolute;
    left: 250px;
    width: 700px;
    height: 400px;
    background: var(--card);
    border-radius: 22px;
    overflow: hidden;
  }
  .card--back { top: 40px; }
  .card--front { top: 467px; }

  /* Back side */
  .crew-photo {
    position: absolute; left: 0; top: 0; width: 700px; height: 175px;
    background: linear-gradient(100deg, var(--photo-warm-b) 0%, #6d6a61 35%, var(--photo-warm-a) 80%, #f7d46c 100%);
  }
  .company-name {
    position: absolute; left: 0; right: 0; top: 190px;
    text-align: center; font-size: 38px; letter-spacing: 2px;
  }
  .company-tagline {
    position: absolute; left: 0; right: 0; top: 236px;
    text-align: center; font-size: 14px; letter-spacing: 1.5px;
  }
  .services {
    position: absolute; left: 0; right: 0; top: 262px;
    display: flex; justify-content: center; font-size: 14px; letter-spacing: 1px; line-height: 21px;
  }
  .services__col { width: 130px; }
  .services__col--left { text-align: right; padding-right: 18px; border-right: 1.5px solid var(--rule); }
  .services__col--right { padding-left: 18px; }
  .slogan {
    position: absolute; left: 0; right: 0; top: 336px;
    text-align: center; font-family: "Montserrat", sans-serif; font-weight: 800; font-size: 17px; letter-spacing: 1px;
  }
  .quote-line {
    position: absolute; left: 0; right: 0; top: 362px;
    text-align: center; font-family: "Montserrat", sans-serif; font-size: 14px; letter-spacing: 1px;
  }
  .quote-line strong { font-weight: 800; }

  /* Front side */
  .repair-tiles {
    position: absolute; left: 20px; top: 22px; display: flex; gap: 12px;
  }
  .repair-tile { width: 100px; height: 100px; border-radius: 16px; }
  .tile-1 { background: linear-gradient(135deg, var(--photo-cool-a), #2f4e7a); }
  .tile-2 { background: linear-gradient(135deg, var(--photo-wood-b), var(--photo-wood-a)); }
  .tile-3 { background: linear-gradient(135deg, #e7e3dc, #b99b7a); }
  .tile-4 { background: linear-gradient(135deg, var(--photo-wood-a), #8a5a35); }
  .tile-5 { background: linear-gradient(135deg, #3f63b3, #e2c257); }
  .tile-6 { background: linear-gradient(135deg, var(--photo-cool-b), #8b9197); }
  .headline {
    position: absolute; left: 30px; top: 142px; font-size: 33px; letter-spacing: 1px;
  }
  .headline-sub {
    position: absolute; left: 220px; top: 184px; font-size: 14px; letter-spacing: 1.5px;
  }
  .headline-rule {
    position: absolute; left: 30px; right: 30px; top: 207px; border-top: 1.5px solid var(--rule);
  }
  .owner {
    position: absolute; left: 30px; top: 232px; padding-bottom: 6px; border-bottom: 1.5px solid var(--rule); width: 260px;
  }
  .owner__name { font-size: 28px; font-variant: small-caps; letter-spacing: 1px; }
  .owner__role { font-size: 14px; margin-top: 2px; }
  .owner-quote {
    position: absolute; left: 30px; top: 330px; font-family: "Montserrat", sans-serif; font-size: 14px; letter-spacing: 1px; line-height: 22px;
  }
  .owner-quote strong { font-weight: 800; }
  .contact-divider {
    position: absolute; left: 400px; top: 232px; height: 90px; border-left: 1.5px solid var(--rule);
  }
  .contact {
    position: absolute; left: 418px; top: 240px; font-size: 13px; letter-spacing: .5px; line-height: 22px;
  }
</style>
</head>
<body>
  <section class="card card--back">
    <div class="crew-photo" role="img" aria-label="Photo of smiling home repairmen in hard hats and safety vests"></div>
    <h1 class="company-name">THE CORNERSTONE FIXERS</h1>
    <p class="company-tagline">DWELLINGS &amp; LODGING</p>
    <div class="services">
      <div class="services__col services__col--left">PLUMBING<br>FLOORING<br>ELECTRICAL</div>
      <div class="services__col services__col--right">PAINTING<br>DRY WALL<br>LANDSCAPING</div>
    </div>
    <p class="slogan">WE CAN HELP | HOME REPAIR | MADE EASY!</p>
    <p class="quote-line">GET YOUR <strong>FREE</strong> QUOTE TODAY! - +555 314 8826</p>
  </section>

  <section class="card card--front">
    <div class="repair-tiles">
      <div class="repair-tile tile-1" role="img" aria-label="Photo of a worker repairing a house exterior"></div>
      <div class="repair-tile tile-2" role="img" aria-label="Photo of roof framing repair"></div>
      <div class="repair-tile tile-3" role="img" aria-label="Photo of plumbing pipes and tools"></div>
      <div class="repair-tile tile-4" role="img" aria-label="Photo of a wooden floor being laid"></div>
      <div class="repair-tile tile-5" role="img" aria-label="Photo of paint cans and brushes"></div>
      <div class="repair-tile tile-6" role="img" aria-label="Photo of drywall panels"></div>
    </div>
    <h2 class="headline">WE SOLVE ALL YOUR REPAIR NEEDS</h2>
    <p class="headline-sub">DWELLINGS &amp; LODGING</p>
    <div class="headline-rule"></div>
    <div class="owner">
      <p class="owner__name">Dorian Pellham</p>
      <p class="owner__role">Owner</p>
    </div>
    <p class="owner-quote">GET YOUR <strong>FREE</strong> QUOTE TODAY!<br>+555 314 8826</p>
    <div class="contact-divider"></div>
    <p class="contact">DORIANPELLHAM047@POSTLINE.NET<br>WWW.THECORNERSTONEFIXERS.COM</p>
  </section>
</body>
</html>
```